Amber Orchard (instructional dating book)

Title: Amber Orchard
Subtitle: Where to plant tulips along a crooked brick path
Author: R.K. Tolvane
I'm seeking the title to be central with the subtitle underneath and the author slightly lower and to the left. Perhaps a border or two around the font. I thought the background could look aged (off color and old textured paper) and the background slightly punched into the texture like a typewriter has been used. I imagine it something like an old Pemberworth playbook or 1940s morse code manual. Many thanks!

Target Market(s)

18 to 45 year old single people

Industry/Entity Type

Dating

Font styles to use
Serif

Requirements
Must have
• Text with border or two
Nice to have
• Traditional feel. The book is instructional.
Should not have
• Too much color or flair

```html
<!DOCTYPE html>
<html lang="en">
<head>
<meta charset="utf-8">
<title>Amber Orchard — R.K. Tolvane</title>
<link href="https://fonts.googleapis.com/css2?family=Special+Elite&family=Libre+Baskerville&display=swap" rel="stylesheet">
<style>
  :root {
    --backdrop: #34323e;
    --cover-white: #ffffff;
    --paper-light: #e2b67c;
    --paper-mid: #d29e60;
    --paper-dark: #b47840;
    --burnt-edge: #7e3f1c;
    --ink-black: #151210;
    --ink-oxblood: #4a120c;
    --author-white: #fffaf2;
  }
  html, body {
    margin: 0;
    width: 1200px;
    height: 776px;
    overflow: hidden;
    background: var(--backdrop);
  }
  .book-cover {
    position: absolute;
    left: 358px;
    top: 38px;
    width: 484px;
    height: 700px;
    background: var(--cover-white);
  }
  .paper-sheet {
    position: absolute;
    inset: 0;
    width: 484px;
    height: 700px;
  }
  .title {
    position: absolute;
    margin: 0;
    font-family: "Special Elite", "Courier New", monospace;
    font-weight: 400;
    text-transform: uppercase;
    line-height: 1;
    white-space: nowrap;
  }
  .title-first {
    left: 82px;
    top: 268px;
    font-size: 76px;
    color: var(--ink-black);
    letter-spacing: 1px;
    -webkit-text-stroke: 1.5px var(--ink-black);
  }
  .title-second {
    left: 58px;
    top: 326px;
    font-size: 84px;
    color: var(--ink-oxblood);
    letter-spacing: 0;
    -webkit-text-stroke: 1.5px var(--ink-oxblood);
  }
  .subtitle {
    position: absolute;
    left: 226px;
    top: 412px;
    width: 240px;
    margin: 0;
    font-family: "Special Elite", "Courier New", monospace;
    font-size: 13.5px;
    line-height: 17px;
    color: var(--ink-black);
  }
  .author {
    position: absolute;
    left: 0;
    right: 0;
    top: 612px;
    margin: 0;
    text-align: center;
    font-family: "Libre Baskerville", "Times New Roman", serif;
    font-size: 40px;
    color: var(--author-white);
    letter-spacing: 0.5px;
  }
</style>
</head>
<body>
  <main class="book-cover">
    <svg class="paper-sheet" viewBox="0 0 484 700" role="img" aria-label="Aged, stained parchment paper with torn, scorched edges">
      <defs>
        <radialGradient id="paperTone" cx="50%" cy="45%" r="70%">
          <stop offset="0%" stop-color="var(--paper-light)"/>
          <stop offset="60%" stop-color="var(--paper-mid)"/>
          <stop offset="100%" stop-color="var(--paper-dark)"/>
        </radialGradient>
      </defs>
      <path fill="url(#paperTone)" stroke="var(--burnt-edge)" stroke-width="2"
        d="M6 0 H478 L476 40 L481 80 L474 120 L479 170 L471 210 L478 260 L472 300
           L480 350 L475 400 L470 430 L476 470 L469 520 L474 560 L466 600 L472 640 L468 700
           H2 L4 660 L1 620 L6 580 L3 540 L7 500 L2 460 L6 420 L3 380 L8 340 L4 300
           L9 260 L5 220 L10 180 L6 140 L11 100 L7 60 L12 20 Z"/>
    </svg>
    <h1 class="title title-first">Amber</h1>
    <h1 class="title title-second">Orchard</h1>
    <p class="subtitle">Where to plant tulips along<br>a crooked brick path</p>
    <p class="author">R.K. Tolvane</p>
  </main>
</body>
</html>
```